SEHLAN REAL ESTATE
شركة السهلان العقارية
Creative Brief
Simple
FAISAL ALQUDRANI
Real Estate Consultant & Developer
12 PALM ROAD, NORAH
f_alqudrani@mailvesta.com
THE LOGO
Yasahiro17 Yasahiro17
YADESIGN YADESIGN

```html
<!DOCTYPE html>
<html lang="en">
<head>
<meta charset="utf-8">
<title>Sehlan Real Estate – Business Cards</title>
<link href="https://fonts.googleapis.com/css2?family=Cinzel:wght@400;600&family=Amiri:wght@400&display=swap" rel="stylesheet">
<style>
  :root {
    --backdrop: #f3f3f3;
    --card: #ffffff;
    --brand-blue: #2f7fbf;
    --ink: #4a4a4a;
    --ink-soft: #7a7a7a;
  }
  html, body {
    margin: 0;
    padding: 0;
    width: 1200px;
    height: 871px;
    overflow: hidden;
    background: var(--backdrop);
  }
  .canvas {
    position: relative;
    width: 1200px;
    height: 871px;
    font-family: "Cinzel", "Times New Roman", serif;
  }
  .card {
    position: absolute;
    top: 319px;
    width: 403px;
    height: 228px;
    background: var(--card);
    box-shadow: 0 1px 4px rgba(0,0,0,0.12);
  }
  .card--front { left: 173px; }
  .card--back  { left: 624px; }

  /* front */
  .front-mark {
    position: absolute;
    left: 42px;
    top: 92px;
    display: flex;
    align-items: center;
    gap: 6px;
    color: var(--brand-blue);
    font-weight: 600;
    font-size: 20px;
    letter-spacing: 1px;
  }
  .mark-square {
    width: 12px;
    height: 12px;
    background: var(--brand-blue);
    flex: none;
  }
  .holder {
    position: absolute;
    left: 192px;
    top: 62px;
  }
  .holder-name {
    font-size: 15px;
    color: var(--ink);
    letter-spacing: 0.5px;
    margin: 0;
    font-weight: 400;
  }
  .holder-role {
    font-size: 6.5px;
    color: var(--ink-soft);
    margin: 3px 0 0;
    letter-spacing: 0.3px;
  }
  .contacts {
    position: absolute;
    left: 196px;
    top: 116px;
    list-style: none;
    margin: 0;
    padding: 0;
  }
  .contacts li {
    display: flex;
    align-items: center;
    gap: 10px;
    height: 24px;
    font-size: 8px;
    color: var(--ink);
    letter-spacing: 0.3px;
    white-space: nowrap;
  }
  .contacts svg { width: 12px; height: 12px; fill: var(--brand-blue); flex: none; }

  /* back */
  .back-lockup {
    position: absolute;
    left: 84px;
    top: 70px;
    display: flex;
    align-items: center;
    gap: 14px;
  }
  .back-lockup .mark-square { width: 42px; height: 42px; }
  .wordmark-latin {
    font-size: 31px;
    font-weight: 400;
    letter-spacing: 1px;
    line-height: 1;
    color: var(--ink);
    text-align: center;
  }
  .wordmark-sub {
    font-size: 8px;
    letter-spacing: 3px;
    color: var(--brand-blue);
    text-align: center;
    margin-top: 3px;
  }
  .wordmark-arabic {
    font-family: "Amiri", "Times New Roman", serif;
    font-size: 24px;
    color: var(--ink);
    line-height: 1.15;
    direction: rtl;
    text-align: center;
    white-space: nowrap;
  }
</style>
</head>
<body>
<div class="canvas">

  <section class="card card--front">
    <div class="front-mark"><span class="mark-square"></span>SEHLAN</div>
    <div class="holder">
      <h1 class="holder-name">FAISAL ALQUDRANI</h1>
      <p class="holder-role">Real Estate Consultant &amp; Developer</p>
    </div>
    <ul class="contacts">
      <li>
        <svg viewBox="0 0 12 12" aria-hidden="true"><path d="M6 1 L11 5.5 H9.5 V11 H7 V8 H5 V11 H2.5 V5.5 H1 Z"/></svg>
        12 PALM ROAD, NORAH
      </li>
      <li>
        <svg viewBox="0 0 12 12" aria-hidden="true"><path d="M3 1 L5 3.5 L4 5 C4.7 6.5 5.5 7.3 7 8 L8.5 7 L11 9 L9.5 11 C5 10.5 1.5 7 1 2.5 Z"/></svg>
        +966500142733
      </li>
      <li>
        <svg viewBox="0 0 12 12" aria-hidden="true"><path d="M1 2.5 H11 V9.5 H1 Z M1.8 3.2 L6 6.3 L10.2 3.2 Z" fill-rule="evenodd"/></svg>
        f_alqudrani@mailvesta.com
      </li>
    </ul>
  </section>

  <section class="card card--back">
    <div class="back-lockup">
      <span class="mark-square"></span>
      <div class="wordmark">
        <div class="wordmark-latin">SEHLAN</div>
        <div class="wordmark-sub">REAL ESTATE</div>
        <div class="wordmark-arabic">شركة السهلان العقارية</div>
      </div>
    </div>
  </section>

</div>
</body>
</html>
```